The Drifters

Copper Heron Productions is looking for their theatrical poster for their film 'THE DRIFTERS'... It is a zombie appocalypse action film made in NSW Australia. See their facebook page www.pagebook.example/THEDRIFTERSFILM...
Updates
Project Deadline Extended
Reason: i have decided to EXTEND the deadline for 5 more days, as there are some really talented artists reviewing their submissions for us... Thank you to all...
Please review the new uploaded images you may or may not want to use to revierw your submissions
Logo Text
Copper Heron Productions
Look and feel
Each slider illustrates characteristics of the customer's brand and the style your logo design should communicate.

```html
<!DOCTYPE html>
<html lang="en">
<head>
<meta charset="utf-8">
<title>The Drifters – Poster</title>
<link href="https://fonts.googleapis.com/css2?family=Abril+Fatface&family=Cinzel:wght@500&family=Oswald:wght@400&display=swap" rel="stylesheet">
<style>
  :root {
    --page-bg: #e8e9e9;
    --ground-light: #55705f;
    --ground-mid: #2f4a3d;
    --ground-dark: #0e1813;
    --ink-white: #f4f4f1;
    --ink-soft: #c9d2cc;
  }
  html, body {
    margin: 0;
    padding: 0;
    width: 1200px;
    height: 1180px;
    overflow: hidden;
    background: var(--page-bg);
  }
  .poster {
    position: absolute;
    left: 200px;
    top: 23px;
    width: 800px;
    height: 1134px;
    overflow: hidden;
    background: var(--ground-dark);
  }
  .poster__photo {
    position: absolute;
    inset: 0;
    background:
      radial-gradient(ellipse 60% 45% at 48% 40%, var(--ground-light) 0%, var(--ground-mid) 55%, transparent 100%),
      radial-gradient(ellipse 80% 70% at 50% 55%, var(--ground-mid) 0%, var(--ground-dark) 100%);
  }
  .poster__tagline {
    position: absolute;
    top: 40px;
    left: 0;
    right: 0;
    margin: 0;
    text-align: center;
    font-family: "Cinzel", serif;
    font-weight: 500;
    font-size: 24px;
    letter-spacing: 0.22em;
    color: var(--ink-white);
  }
  .poster__title {
    position: absolute;
    inset: 0;
    width: 800px;
    height: 1134px;
  }
  .poster__title text {
    font-family: "Abril Fatface", serif;
    fill: var(--ink-white);
  }
  .poster__release {
    position: absolute;
    left: 532px;
    top: 940px;
    margin: 0;
    font-family: "Oswald", sans-serif;
    font-size: 30px;
    letter-spacing: 0.04em;
    color: var(--ink-white);
  }
  .poster__synopsis {
    position: absolute;
    left: 520px;
    top: 990px;
    width: 250px;
    margin: 0;
    font-family: "Oswald", sans-serif;
    font-size: 9.5px;
    line-height: 1.35;
    color: var(--ink-soft);
  }
</style>
</head>
<body>
  <main class="poster">
    <div class="poster__photo" role="img" aria-label="Photograph of wet pavement in the rain, a person's feet walking at the top with their long reflection stretching down the puddle"></div>

    <p class="poster__tagline">IT’S KILL OR BE KILLED</p>

    <svg class="poster__title" viewBox="0 0 800 1134" aria-label="THE DRIFTERS">
      <text class="poster__title-the" x="360" y="668" font-size="150" textLength="330" lengthAdjust="spacingAndGlyphs" transform="rotate(-28 360 668)">THE</text>
      <text class="poster__title-main" x="58" y="1032" font-size="150" textLength="760" lengthAdjust="spacingAndGlyphs" transform="rotate(-28 58 1032)">DRIFTERS</text>
    </svg>

    <p class="poster__release">COMING SOON</p>

    <p class="poster__synopsis">A quiet coastal town wakes to find its streets overrun by the restless dead. With the roads closed and the radios silent, a small band of survivors must cross the flooded valley before nightfall. Every step leaves a trace, and every trace can be followed. Filmed on location across regional New South Wales, this gripping story follows strangers forced to trust each other as the world they knew slips away beneath the rain.</p>
  </main>
</body>
</html>
```